Business Card Design for a Private Label Pet Company

We need a business card design for our family-owned company, Harbor Paw Works (www.harborpawworks-example.com), out of St. Louis, MO. We provide turnkey private label solutions for retailers, Cartwell sellers and other brands who want to provide high quality, natural, Made in the USA pet products to their customers. Our customer are worldwide and range from the US to the UK to Vietnam and beyond. We offer private label for dozens of pet products including grooming products (shampoos, conditioners, colognes, ear and eye washes, mouthwash, etc.), all meat treats, supplements, and specialty products (pet stain and odor cleaner, anti-chew spray, etc.). We would like to see designs that use the colors, fonts and logos (see variations) within our brand guidelines and fit with the look and feel from our website.

Target Market(s)

Pet Store Owners, Cartwell Sellers, Pet Brand Marketers

Industry/Entity Type

Pet

Contact Information for Business Card

Lyle Dorsett
CEO
Harbor Paw Works
5817 Wexmoor Commerce Lane
St. Louis, MO 63188
office: 314.555.0182
mobile: 770.555.0139
email: lyle@harborpawworks-example.com

Colors

Designer to choose colors to be used in the design.

Requirements
Must have
• Need to follow the brand guidelines attached for colors, fonts and logos
• Need to use the logos attached (or a variation) with our without the tagline
• Name, title, phone (office and mobil), email, address on the business card
• Clean professional look and feel that says: high quality natural pet products, high quality service, made in the USA
Nice to have
• Made in the USA is a big positive in our industry and we are very proud of it. There is an attached icon from our website. The designer can get creative here as they wish.
• I do like using color for pop. Just don't like lots of bright, loud colors.
Should not have
• lots of bright, loud colors
• overwhelming to the reader
• crowded

```html
<!DOCTYPE html>
<html lang="en">
<head>
<meta charset="utf-8">
<title>Harbor Paw Works — Business Card</title>
<link rel="stylesheet" href="https://fonts.googleapis.com/css2?family=Oswald:wght@500;600&family=Questrial&display=swap">
<style>
  :root {
    --page-bg: #e9e7e2;
    --card-white: #fbfbfa;
    --slate: #4b6462;
    --slate-back: #4d6664;
    --leaf: #5f7b35;
    --body-grey: #5a5d5e;
    --paw-tint: #ebeae7;
    --white: #ffffff;
  }
  * { margin: 0; padding: 0; box-sizing: border-box; }
  html, body { width: 1200px; height: 960px; overflow: hidden; }
  body { background: var(--page-bg); position: relative; font-family: "Questrial", sans-serif; }

  .card {
    position: absolute;
    width: 600px;
    height: 343px;
    overflow: hidden;
    box-shadow: 0 2px 6px rgba(0,0,0,0.18);
  }

  /* Front */
  .card-front { left: 302px; top: 129px; background: var(--card-white); }
  .paw-watermark {
    position: absolute;
    left: 285px; top: 5px;
    width: 310px; height: 335px;
    background: radial-gradient(ellipse at 55% 60%, var(--paw-tint) 0%, var(--paw-tint) 45%, rgba(235,234,231,0) 72%);
  }
  .brand-name {
    position: absolute;
    left: 36px; top: 34px;
    font-family: "Oswald", sans-serif;
    font-weight: 600;
    font-size: 38px;
    line-height: 1;
    letter-spacing: 0.5px;
    color: var(--slate);
    text-transform: uppercase;
  }
  .contact {
    position: absolute;
    left: 39px; top: 217px;
    font-size: 13.5px;
    line-height: 16.5px;
    color: var(--body-grey);
  }
  .contact .address { margin-bottom: 4px; }
  .person {
    position: absolute;
    right: 42px; top: 241px;
    text-align: right;
    font-family: "Oswald", sans-serif;
    font-weight: 500;
    text-transform: uppercase;
    line-height: 1;
  }
  .person-name { font-size: 21px; color: var(--slate); letter-spacing: 0.3px; }
  .person-title { font-size: 16px; color: var(--leaf); margin-top: 3px; }
  .edge-tab {
    position: absolute;
    right: 0; top: 244px;
    width: 10px; height: 37px;
    background: var(--slate);
  }

  /* Back */
  .card-back { left: 299px; top: 488px; background: var(--slate-back); }
  .paw-pattern { position: absolute; inset: 0; background: var(--slate-back); }
  .usa-badge {
    position: absolute;
    left: 513px; top: 25px;
    width: 57px; height: 47px;
    background: var(--white);
  }
  .back-brand {
    position: absolute;
    left: 0; right: 0; top: 104px;
    text-align: center;
    font-family: "Oswald", sans-serif;
    font-weight: 600;
    font-size: 46px;
    line-height: 1;
    letter-spacing: 0.5px;
    color: var(--white);
    text-transform: uppercase;
  }
  .back-rule {
    position: absolute;
    left: 137px; top: 197px;
    width: 310px;
    height: 4px;
    border-top: 1px solid rgba(255,255,255,0.8);
    border-bottom: 1px solid rgba(255,255,255,0.8);
  }
  .website {
    position: absolute;
    left: 0; right: 0; top: 210px;
    text-align: center;
    font-size: 13.5px;
    letter-spacing: 2.2px;
    color: var(--white);
  }
  .social-row { position: absolute; left: 208px; top: 278px; }
</style>
</head>
<body>

<section class="card card-front" aria-label="Business card front">
  <div class="paw-watermark" role="img" aria-label="Large faint brand paw mark"></div>
  <div class="brand-name">Harbor Paw Works</div>
  <div class="contact">
    <p class="address">5817 Wexmoor Commerce Lane<br>St. Louis, MO 63188</p>
    <p>Office: 314.555.0182<br>Mobile: 770.555.0139<br>lyle@harborpawworks-example.com</p>
  </div>
  <div class="person">
    <div class="person-name">Lyle Dorsett</div>
    <div class="person-title">CEO</div>
  </div>
  <div class="edge-tab"></div>
</section>

<section class="card card-back" aria-label="Business card back">
  <div class="paw-pattern" role="img" aria-label="Faint repeating paw pattern"></div>
  <div class="usa-badge" role="img" aria-label="Made in the USA badge"></div>
  <div class="back-brand">Harbor Paw Works</div>
  <div class="back-rule"></div>
  <div class="website">www.harborpawworks-example.com</div>
  <svg class="social-row" width="184" height="24" viewBox="0 0 184 24" aria-label="Social media links">
    <line x1="0" y1="12" x2="64" y2="12" stroke="#ffffff" stroke-opacity="0.8" stroke-width="1"/>
    <circle cx="77" cy="12" r="10.5" fill="#ffffff"/>
    <circle cx="103" cy="12" r="10.5" fill="#ffffff"/>
    <line x1="120" y1="12" x2="184" y2="12" stroke="#ffffff" stroke-opacity="0.8" stroke-width="1"/>
  </svg>
</section>

</body>
</html>
```